Herbal Apothecary Rebrand

I am in the process of merging two companies Wren Hollow Oils and Among The Pines Apothecary. I am dissolving Wren Hollow Oils (WHO) and need to blend a few of the products into the Among The Pines Apothecary (ATP) line. These blended products will take on a fresh new look. This is where I need some help. I have a few ideas but need some creative genius to bring them together.
The following products need to be merged and once a logo is agreed upon I will be working with this designer with further pay to create the following:
~ body oils (labels and packaging) **existing product shown in image A-1
~ plant bath medicines (labels and packaging) **a new product with the bottle and packaging shown in images attached
~ facial serum (labels and packaging - the packaging will be the same cardboard boxes used for the body oils) **existing product shown in
image A-2
~ teas (labeling) **a new product - packaging sample pics attached
~ as well as having the ability to carry over into the creation of 40 different essential oil containers. ** An idea I have is shown in image C-1.
Ideas...
I prefer distinct lines, square designs vs circular or curvy. I prefer clean and clear vs busy.
I like the layout shown in images A-1 & A-2 and could see moving forward with a very similar style without the indigenous logo. I would like to see what it looks like to have the ATP logo (building with trees) in place of the indigenous logo. ** I am open to reworking the ATP logo to make it a bit more vertical in size vs being quite small and horizontal. This could include revising or recreating the building and trees altogether.
I like the speckled background (shown in image B-1), it gives the sense that it is aged and goes with the Apothecary theme, however I'm not completely attached to it.
I like the off white labels that I currently have for the BODY OILS and the SERUM and I am leaning towards this as the colour for the new blended line. I would also be open to seeing a lighter version of the turquoise.
This is just an idea that I have however I am open to something completely new. What is important is that it blends nicely with the current line of products available at ATP (the entire line can be seen online). There is a good chance that I will be merging the products over to the new and improved design as we move through the older packaging.
Notes on Plant Bath labels:
**If working from the current layout of the Body Oil labels this can be used as an example to create a template
~ The top will have the new or reworked logo (with or without the company name depending on space available)
~ First line for each bottle will have a name eg: NETTLE + ROSE
~ Second line will be the purpose of the medicine eg: HEART OPENING
~ The next line will read: PLANT BATH
~Then space for a little blurb eg: BRINGING BALANCE TO THE EMOTIONAL AND ENERGETIC HEALTH OF THE HEART.
~ The size of the bottle will read 400 ML but in a vertical direction on the bottle
Notes on Tea labels:
The teas have not been created yet but I'm looking for some ideas that follow in the same design as the Plant Bath labels so the following can be used as an example:
~ Name; TULSI + ROSE
~ The purpose: ELEVATED HEART
~ The bottom will read: LOOSE TEA
~ Blurb about the benefits: A TRANSFORMATIONAL CREATION OF WARM NOTES WITH DEEP WOODY UNDERTONES. THIS ANYTIME TEA IS AS PLEASING IN THE HEALTH BENEFITS AS IT IS TO THE TASTE.
~ Include the size: 100g
**I maxed out in pictures so I wasn't able to add more inspiration pics but I also quite like the moss & kettle tea line (shows up in a google search) as its clean and clear. The difference being I won't be printing directly on the packaging, it will need to be a label.
Logo Text
I would like to see if we can incorporate the name AMONG THE PINES APOTHECARY however this might make it too busy. Perhaps smaller lettering for "among the pines" and larger for "APOTHECARY". It also might be the case that adding this on the front makes things look too busy. I'm open to creative suggestions.

```html
<!DOCTYPE html>
<html lang="en">
<head>
<meta charset="utf-8">
<title>Nettle + Rose Plant Bath Label</title>
<link rel="stylesheet" href="https://fonts.googleapis.com/css2?family=Fira+Sans:wght@400&family=Raleway:wght@300&display=swap">
<style>
  :root {
    --page: #ffffff;
    --label-teal: #33b3a6;
    --scene-tone: #2a9c90;
    --ink: #4a3a36;
  }
  html, body {
    margin: 0;
    padding: 0;
    width: 1200px;
    height: 1179px;
    overflow: hidden;
    background: var(--page);
  }
  .label {
    position: absolute;
    left: 156px;
    top: 90px;
    width: 888px;
    height: 1000px;
    background: var(--label-teal);
    color: var(--ink);
  }
  .brand-small,
  .brand-large {
    position: absolute;
    left: 328px;
    width: 400px;
    margin: 0;
    text-align: center;
    font-family: "Raleway", sans-serif;
    font-weight: 300;
    color: var(--ink);
    line-height: 1;
    white-space: nowrap;
  }
  .brand-small {
    top: 150px;
    font-size: 20px;
    letter-spacing: 0.32em;
  }
  .brand-large {
    top: 268px;
    font-size: 46px;
    letter-spacing: 0.06em;
  }
  .brand-scene {
    position: absolute;
    left: 380px;
    top: 186px;
    width: 306px;
    height: 62px;
    background: linear-gradient(180deg, var(--label-teal), var(--scene-tone));
  }
  .rule {
    position: absolute;
    left: 164px;
    width: 565px;
    height: 2px;
    background: var(--ink);
  }
  .rule-name { top: 527px; }
  .rule-purpose { top: 606px; }
  .rule-type { top: 698px; }
  .rule-bottom { top: 932px; }
  .product-name,
  .product-purpose {
    position: absolute;
    left: 164px;
    margin: 0;
    font-family: "Fira Sans", sans-serif;
    font-weight: 400;
    line-height: 1;
    white-space: nowrap;
  }
  .product-name { top: 472px; font-size: 46px; letter-spacing: 0.08em; }
  .product-purpose { top: 554px; font-size: 40px; letter-spacing: 0.09em; }
  .product-type {
    position: absolute;
    left: 164px;
    top: 650px;
    margin: 0;
    font-family: "Raleway", sans-serif;
    font-weight: 300;
    font-size: 30px;
    letter-spacing: 0.02em;
    line-height: 1;
  }
  .blurb {
    position: absolute;
    left: 158px;
    top: 732px;
    width: 394px;
    margin: 0;
    font-family: "Raleway", sans-serif;
    font-weight: 300;
    font-size: 30px;
    line-height: 40px;
    letter-spacing: 0.02em;
  }
  .blurb-line {
    display: block;
    text-align: justify;
    text-align-last: justify;
    white-space: nowrap;
  }
  .blurb-line:last-child { text-align-last: left; }
  .divider {
    position: absolute;
    left: 600px;
    top: 716px;
    width: 2px;
    height: 172px;
    background: var(--ink);
  }
  .volume {
    position: absolute;
    left: 685px;
    top: 805px;
    margin: 0;
    font-family: "Fira Sans", sans-serif;
    font-weight: 400;
    font-size: 34px;
    letter-spacing: 0.04em;
    line-height: 1;
    white-space: nowrap;
    transform: translate(-50%, -50%) rotate(-90deg);
  }
</style>
</head>
<body>
  <main class="label">
    <p class="brand-small">AMONG THE PINES</p>
    <div class="brand-scene" role="img" aria-label="Engraved farmstead scene with barns, silo and trees"></div>
    <p class="brand-large">APOTHECARY</p>

    <h1 class="product-name">NETTLE + ROSE</h1>
    <div class="rule rule-name"></div>

    <h2 class="product-purpose">HEART OPENING</h2>
    <div class="rule rule-purpose"></div>

    <p class="product-type">PLANT BATH</p>
    <div class="rule rule-type"></div>

    <p class="blurb">
      <span class="blurb-line">BRINGING BALANCE TO</span>
      <span class="blurb-line">THE EMOTIONAL AND</span>
      <span class="blurb-line">ENERGETIC HEALTH</span>
      <span class="blurb-line">OF THE HEART.</span>
    </p>
    <div class="divider"></div>
    <p class="volume">400 ML</p>

    <div class="rule rule-bottom"></div>
  </main>
</body>
</html>
```